2020 C FILM FESTIVAL CAMPAIGN

Theme: 20/20 Vision
"For the 2020 Calverick Film Festival, we are looking at the vision of the festival as well as filmmaking. We are asking Designers to recreate an Eye Chart Test. The first row/letter (typically 'E') will be where the Logo goes, the second row will have 20 20 pay attention to the spacing between the '20s, the third row will have the letters CFF again note the spacing. These first three lines ideally are creating a pyramid. We are looking for a funky grime kind of font for "CFF & 2020". Instead of letters, we want to use symbols and the chart gets smaller in text. We the following symbols should be the largest on the chart a "Black Power Fist" "Female Symbol" Transgender Symbol" "recycling symbol". All over symbols should relate to Film and Cinema and the fine arts.

Font styles to use
Sans Serif
Decorative

Colors

Designer to choose colors to be used in the design.

Requirements
Nice to have
• Fancy fonts

```html
<!DOCTYPE html>
<html lang="en">
<head>
<meta charset="utf-8">
<title>Calverick Film Festival 2020 – Eye Chart</title>
<link rel="stylesheet" href="https://fonts.googleapis.com/css2?family=Montserrat:wght@700&family=Roboto+Slab:wght@800&family=Josefin+Sans:wght@400;600&family=Roboto:wght@400&display=swap">
<style>
  :root {
    --backdrop: #ecebe8;
    --chart-paper: #ffffff;
    --chart-edge: #b9b9b9;
    --ink: #1f1c1d;
    --muted-ink: #333333;
    --teal: #3f9fae;
    --festival-red: #b5222b;
    --festival-gold: #e8a531;
    --strip-green: #8fb26a;
    --strip-orange: #e07f4a;
  }
  * { margin: 0; padding: 0; box-sizing: border-box; }
  html, body { width: 1200px; height: 900px; overflow: hidden; }
  body { background: var(--backdrop); position: relative; font-family: "Roboto", sans-serif; }

  .eye-chart {
    position: absolute; left: 403px; top: 57px; width: 395px; height: 787px;
    background: var(--chart-paper); border: 1px solid var(--chart-edge); border-radius: 20px;
    color: var(--ink);
  }
  .chart-row {
    position: absolute; left: 0; right: 0; display: flex;
    justify-content: center; align-items: center;
  }
  .acuity-label {
    position: absolute; left: 14px; font-size: 7px; line-height: 1.25; color: var(--muted-ink);
    transform: translateY(-50%);
  }
  .acuity-label small { display: block; font-size: 5px; }
  .row-number {
    position: absolute; right: 24px; font-size: 13px; color: var(--muted-ink);
    transform: translateY(-50%);
  }

  .festival-name {
    gap: 12px; top: 88px; height: 60px;
  }
  .festival-dot { width: 22px; height: 22px; border-radius: 50%; background: var(--festival-gold); flex: none; }
  .festival-name-text {
    font-family: "Josefin Sans", sans-serif; font-weight: 600; font-size: 19px;
    line-height: 1.1; letter-spacing: 1px; color: var(--ink); text-transform: uppercase;
  }

  .year-row {
    top: 203px; height: 80px; gap: 70px;
    font-family: "Montserrat", sans-serif; font-weight: 700; font-size: 86px; line-height: 1;
  }
  .slab { font-family: "Roboto Slab", serif; font-weight: 800; line-height: 1; }
  .slab span { display: inline-flex; justify-content: center; }
  .row-3 { top: 296px; height: 68px; font-size: 63px; }
  .row-3 span { width: 103px; }
  .row-4 { top: 375px; height: 50px; font-size: 45px; }
  .row-4 span { width: 60px; }
  .row-5 { top: 428px; height: 40px; font-size: 35px; }
  .row-5 span { width: 42px; }
  .row-6 { top: 477px; height: 32px; font-size: 28px; }
  .row-6 span { width: 34px; }
  .row-7 { top: 544px; height: 24px; font-size: 21px; }
  .row-7 span { width: 26px; }
  .row-8 { top: 590px; height: 22px; font-size: 18px; }
  .row-8 span { width: 19.5px; }
  .row-9 { top: 648px; height: 16px; font-size: 13px; }
  .row-9 span { width: 17px; }
  .row-10 { top: 692px; height: 14px; font-size: 11px; }
  .row-10 span { width: 14.5px; }

  .chart-icon { background: var(--ink); border-radius: 3px; display: block; }
  .row-5 .chart-icon { width: 30px; height: 26px; border-radius: 50%; }
  .row-6 .chart-icon { width: 21px; height: 20px; }
  .row-7 .chart-icon { width: 15px; height: 15px; }
  .row-8 .chart-icon { width: 13px; height: 13px; }

  .film-strip { position: absolute; height: 14px; border-radius: 1px; }
  .film-strip.green { left: 90px; width: 192px; top: 518px; background: var(--strip-green); }
  .film-strip.orange { left: 97px; width: 200px; top: 619px; background: var(--strip-orange); }

  .festival-dates {
    position: absolute; left: 0; right: 0; top: 734px; text-align: center;
    font-family: "Josefin Sans", sans-serif; font-weight: 400; font-size: 22px;
    letter-spacing: 0.5px; color: var(--teal);
  }
  .festival-dates sup { font-size: 11px; vertical-align: 8px; }
</style>
</head>
<body>
  <main class="eye-chart">
    <div class="acuity-label" style="top:108px">200ft<small>0.10</small></div>
    <div class="acuity-label" style="top:243px">100ft<small>0.20</small></div>
    <div class="acuity-label" style="top:330px">70ft<small>0.28</small></div>
    <div class="acuity-label" style="top:400px">50ft<small>0.40</small></div>
    <div class="acuity-label" style="top:448px">40ft<small>0.50</small></div>
    <div class="acuity-label" style="top:493px">30ft<small>0.66</small></div>
    <div class="acuity-label" style="top:556px">25ft<small>0.80</small></div>
    <div class="acuity-label" style="top:601px">20ft<small>1.00</small></div>
    <div class="acuity-label" style="top:656px">15ft<small>1.33</small></div>
    <div class="acuity-label" style="top:700px">13ft<small>1.45</small></div>

    <div class="row-number" style="top:112px">1</div>
    <div class="row-number" style="top:242px">2</div>
    <div class="row-number" style="top:330px">3</div>
    <div class="row-number" style="top:400px">4</div>
    <div class="row-number" style="top:448px">5</div>
    <div class="row-number" style="top:493px">6</div>
    <div class="row-number" style="top:556px">7</div>
    <div class="row-number" style="top:601px">8</div>
    <div class="row-number" style="top:656px">9</div>
    <div class="row-number" style="top:700px">10</div>

    <div class="chart-row festival-name">
      <span class="festival-dot"></span>
      <span class="festival-name-text">Calverick<br>Film Festival</span>
    </div>

    <div class="chart-row year-row"><span>20</span><span>20</span></div>

    <div class="chart-row slab row-3"><span>C</span><span>F</span><span>F</span></div>
    <div class="chart-row slab row-4"><span>V</span><span>Z</span><span>C</span><span>M</span></div>
    <div class="chart-row slab row-5">
      <span>F</span><span>R</span>
      <span><i class="chart-icon" role="img" aria-label="Laurel wreath with star icon"></i></span>
      <span>N</span><span>G</span>
    </div>
    <div class="chart-row slab row-6">
      <span>I</span>
      <span><i class="chart-icon" role="img" aria-label="Clapperboard icon"></i></span>
      <span>Z</span><span>V</span>
      <span><i class="chart-icon" role="img" aria-label="Theatre masks icon"></i></span>
      <span>F</span>
    </div>
    <div class="film-strip green" role="img" aria-label="Green film strip band"></div>
    <div class="chart-row slab row-7">
      <span><i class="chart-icon" role="img" aria-label="Director's chair icon"></i></span>
      <span>E</span><span>L</span>
      <span><i class="chart-icon" role="img" aria-label="Film camera icon"></i></span>
      <span>P</span><span>Z</span>
      <span><i class="chart-icon" role="img" aria-label="Popcorn icon"></i></span>
    </div>
    <div class="chart-row slab row-8">
      <span>D</span><span>E</span>
      <span><i class="chart-icon" role="img" aria-label="Movie ticket icon"></i></span>
      <span>P</span><span>M</span>
      <span><i class="chart-icon" role="img" aria-label="Film reel icon"></i></span>
      <span>E</span><span>C</span>
    </div>
    <div class="film-strip orange" role="img" aria-label="Orange film strip band"></div>
    <div class="chart-row slab row-9"><span>L</span><span>E</span><span>F</span><span>O</span><span>D</span><span>P</span><span>C</span><span>T</span></div>
    <div class="chart-row slab row-10"><span>F</span><span>D</span><span>P</span><span>L</span><span>T</span><span>C</span><span>E</span><span>O</span></div>

    <p class="festival-dates">MARCH 27<sup>TH</sup> – APRIL 5<sup>TH</sup> 2020</p>
  </main>
</body>
</html>
```